MIRA VANE coconut based Haircare range

I need a label design for my new range of coconut based hair care called Mira Vane.

Mira represents coconut and Vane represents sun.

The label is on a white bottle, so the label you design could be fun and vibrant to represent the brand name.

Tagline: Healthy Happy Hair

The Mira Vane logo needs to be part of this label and hasn't been developed, so feel free to include your design as part of the label.

The winner of this contest will be hired to design additional labels for the other products in the range which includes shampoo, conditioner, hair serum, body lotion, shower gel and massage oil.

Please work on a white pump bottle for shampoo and conditioner for this brief. We do need a theme that will work across all the products in the range.

THE LABEL DIMENSION (WRAP AROUND) 15CM X 11CM
Have fun with this design!

What I am trying to do is get people to envisage that by using this brand they are reminded of GOOD TIMES – HOLIDAYS, FUN, and SUN. Remind them of PARADISE.

We want them to look at the brand and want to buy it because it makes them FEEL GOOD.

This range of luscious, nature based hair products is suitable for every hair type and comes in six refreshing aromas, made with a range of active ingredients including 100% cold-pressed, organic coconut oil.

Thank you for your work!

Target Market(s)

Unisex - people that like fun and natural products

Industry/Entity Type

Hair And Beauty

Colors
0355a3
6b449b
00a990
33a6d7
33b8a4
a6cf38
886aae
a64599

Requirements
Must have
• Vibrant
• Fun
• Logo must work across all products
• Hip
• You can use the words in the file as inspiration or feel free to use the words on the bottle to cultivate a feeling of holidays and this shampoo reminding them of the fun they had.
Nice to have
• A label that can work across different products by changing the colour palette not the whole design
Should not have
• Be too sterile / cold

```html
<!DOCTYPE html>
<html lang="en">
<head>
<meta charset="utf-8">
<title>Mira Vane Nourishing Shampoo Label</title>
<link rel="stylesheet" href="https://fonts.googleapis.com/css2?family=Dancing+Script:wght@500&family=Poppins:wght@300;700&family=Oswald:wght@400&display=swap">
<style>
  :root {
    --label-white: #ffffff;
    --brand-green: #078a2f;
    --art-lime: #d4e43c;
    --art-leaf: #93c843;
    --art-teal: #2fa57c;
    --text-on-band: #ffffff;
  }
  * { margin: 0; padding: 0; box-sizing: border-box; }
  html, body { width: 1200px; height: 893px; overflow: hidden; background: var(--label-white); }
  .label { position: relative; width: 1200px; height: 893px; background: var(--label-white); }
  .hero-art { position: absolute; left: 0; top: 0; width: 1200px; height: 893px; }
  .brand-badge {
    position: absolute; left: 539px; top: 82px; width: 122px; height: 122px;
    border-radius: 50%; background: var(--brand-green);
    display: flex; align-items: center; justify-content: center; text-align: center;
    color: var(--label-white); font-family: "Oswald", sans-serif; font-weight: 400;
    font-size: 18px; line-height: 1.15; letter-spacing: 2px;
  }
  .tagline {
    position: absolute; left: 515px; top: 232px; width: 400px;
    font-family: "Dancing Script", cursive; font-weight: 500; color: var(--label-white);
    font-size: 104px; line-height: 79px;
    text-shadow: 2px 3px 6px rgba(0, 60, 20, 0.3);
  }
  .tagline span { display: block; }
  .tagline .line-2 { padding-left: 55px; }
  .tagline .line-3 { padding-left: 75px; }
  .product-band {
    position: absolute; left: 0; top: 501px; width: 1200px; height: 185px;
    background: var(--brand-green); color: var(--text-on-band);
  }
  .product-benefit {
    position: absolute; left: 479px; top: 13px; line-height: 1;
    font-family: "Poppins", sans-serif; font-weight: 300; font-size: 28px; letter-spacing: 2px;
  }
  .product-type {
    position: absolute; left: 477px; top: 49px; line-height: 1;
    font-family: "Poppins", sans-serif; font-weight: 700; font-size: 42px; letter-spacing: 4px;
  }
  .product-rule {
    position: absolute; left: 479px; top: 104px; width: 362px; height: 2px; background: var(--text-on-band);
  }
  .product-notes {
    position: absolute; left: 479px; top: 114px;
    font-family: "Oswald", sans-serif; font-size: 14px; line-height: 23px; letter-spacing: 0.4px;
  }
  .volume {
    position: absolute; left: 0; width: 1200px; top: 808px; text-align: center;
    font-family: "Oswald", sans-serif; font-size: 15px; letter-spacing: 0.8px; color: var(--brand-green);
  }
</style>
</head>
<body>
<main class="label">
  <svg class="hero-art" viewBox="0 0 1200 893" role="img" aria-label="Watercolour paint splash illustration in lime, leaf green and teal">
    <defs>
      <radialGradient id="hero-wash" cx="0.48" cy="0.5" r="0.5">
        <stop offset="0" stop-color="var(--art-lime)"/>
        <stop offset="0.5" stop-color="var(--art-leaf)"/>
        <stop offset="0.8" stop-color="var(--art-teal)" stop-opacity="0.75"/>
        <stop offset="1" stop-color="var(--art-teal)" stop-opacity="0"/>
      </radialGradient>
    </defs>
    <rect x="78" y="85" width="950" height="705" fill="url(#hero-wash)"/>
  </svg>

  <div class="brand-badge">MIRA<br>VANE</div>

  <h1 class="tagline">
    <span class="line-1">Healthy</span>
    <span class="line-2">happy</span>
    <span class="line-3">Hair</span>
  </h1>

  <section class="product-band">
    <p class="product-benefit">NOURISHING</p>
    <h2 class="product-type">SHAMPOO</h2>
    <div class="product-rule"></div>
    <p class="product-notes">MADE WITH ORGANIC COCONUT OIL<br>FOR NORMAL TO DRY HAIR</p>
  </section>

  <p class="volume">12 FL. OZ. (355ML)</p>
</main>
</body>
</html>
```